FRÜST Cocktails Needs a Flyer Design

We need a flyer designed for our new range of frozen cocktails. The flyer should have the following information and act as an introduction to the brand and products:

All three packs / packshots
All three flavour descriptions (see website under "Our Cocktails")
Social media (fb and twitter) and website references (www.frustcocktails.example)
Consistent with style of website and packaging
Similar copy to homepage of website (Authentic bar-quality cocktails made with the finest natural ingredients. No mixing, no mess, no hassle. Just freeze, squeeze & enjoy!)

The flyer should communicate the premium nature and authenticity of the product in a clean and stylish way.

The flyer size will be DL (210mm x 98mm) and double-sided

Target Market(s)

Adults in the UK aged 25 onwards with a medium to high disposable income

Industry/Entity Type

Media

Requirements
Should not have
• Any tacky elements

```html
<!DOCTYPE html>
<html lang="en">
<head>
<meta charset="utf-8">
<title>FRÜST Cocktails – DL Flyer</title>
<link rel="stylesheet" href="https://fonts.googleapis.com/css2?family=Cabin:wght@500;700&family=PT+Sans+Narrow:wght@400;700&display=swap">
<style>
  :root {
    --backdrop: #54a7c8;
    --ink: #1a1a1a;
    --slate: #3b4656;
    --band: rgba(255,255,255,0.9);
    --sheet: #f6f9fc;
    --cosmo-red: #e2424f;
    --cosmo-orange: #e8931f;
    --mojito-green: #2f9436;
    --mojito-lime: #86b53a;
    --lychee-red: #c3182b;
    --lychee-blush: #f5b9a9;
    --frost: #b9d3e6;
    --pack-cream: #f3ead8;
    --pack-silver: #e4e6e8;
  }
  * { box-sizing: border-box; margin: 0; padding: 0; }
  html, body { width: 1200px; height: 1200px; overflow: hidden; }
  body { background: var(--backdrop); position: relative; font-family: "PT Sans Narrow", sans-serif; }

  .flyer { position: absolute; left: 126px; width: 946px; height: 442px; box-shadow: 0 4px 10px rgba(0,0,0,0.25); overflow: hidden; }
  .flyer--front { top: 118px; }
  .flyer--back { top: 640px; background: linear-gradient(135deg, #ffffff 0%, var(--sheet) 60%, #e9f1f8 100%); }

  /* Front */
  .mountain-photo { position: absolute; inset: 0;
    background: linear-gradient(180deg, #a9c7e2 0%, #d7e5f0 30%, #eef3f7 48%, #9aa9bb 68%, #3f4c5f 85%, #6f7f92 100%); }
  .brand-name { position: absolute; left: 0; right: 0; top: 176px; text-align: center;
    font-family: "Cabin", sans-serif; font-weight: 700; font-size: 92px; letter-spacing: 2px; color: var(--ink); line-height: 1; }
  .strapline-band { position: absolute; left: 0; right: 0; top: 282px; height: 94px; background: var(--band); }
  .strapline { position: absolute; left: 200px; right: 200px; top: 21px; text-align: center;
    font-weight: 700; font-size: 15.5px; line-height: 26px; color: var(--slate); text-transform: uppercase; }
  .strapline__line { display: block; white-space: nowrap; }
  .packshots { position: absolute; top: 8px; display: flex; gap: 8px; }
  .packshots--cartons { left: 26px; }
  .packshots--pouches { right: 28px; }
  .packshot { width: 52px; height: 78px; border-radius: 2px; }
  .packshot--carton { background: linear-gradient(180deg, var(--pack-cream), #fff 70%); box-shadow: 0 1px 3px rgba(0,0,0,0.2); }
  .packshot--pouch { background: linear-gradient(180deg, var(--pack-silver), #fff 65%); border-radius: 6px; box-shadow: 0 1px 3px rgba(0,0,0,0.2); }

  /* Back */
  .flavour { position: absolute; top: 74px; width: 332px; height: 332px; border-radius: 50%;
    border: 3px solid; text-align: center; padding-top: 112px; }
  .flavour--cosmopolitan { left: 39px; border-color: var(--cosmo-red); color: var(--cosmo-red); }
  .flavour--mojito { left: 307px; border-color: var(--mojito-green); color: var(--mojito-green); }
  .flavour--lychee { left: 575px; border-color: var(--lychee-red); color: var(--lychee-red); }
  .flavour__kind { font-family: "Cabin", sans-serif; font-weight: 700; font-size: 30px; line-height: 30px; }
  .flavour__name { font-family: "Cabin", sans-serif; font-weight: 700; font-size: 23px; line-height: 28px; text-transform: uppercase; white-space: nowrap; }
  .flavour--cosmopolitan .flavour__name { color: var(--cosmo-orange); }
  .flavour--mojito .flavour__name { color: var(--mojito-lime); font-size: 28px; }
  .flavour--lychee .flavour__name { color: var(--lychee-blush); }
  .flavour__tagline { font-weight: 700; font-size: 14px; margin-top: 12px; text-transform: uppercase; white-space: nowrap; }
  .flavour__copy { font-size: 13px; line-height: 15px; margin: 8px auto 0; width: 200px; white-space: nowrap; }

  .corner-mark { position: absolute; left: 28px; bottom: 30px; font-family: "Cabin", sans-serif; font-weight: 700; font-size: 22px; color: var(--frost); }

  .contact { position: absolute; left: 0; right: 0; bottom: 14px; display: flex; justify-content: center; align-items: center; gap: 16px;
    font-weight: 700; font-size: 13px; color: var(--slate); }
  .contact__item { display: flex; align-items: center; gap: 7px; }
  .contact__dot { width: 20px; height: 20px; border-radius: 50%; background: var(--slate); }
  .contact__dot--twitter { background: #6aa6d6; }
  .contact__divider { color: var(--slate); }
</style>
</head>
<body>

<section class="flyer flyer--front">
  <div class="mountain-photo" role="img" aria-label="Photograph of snow-capped mountain peaks under a pale blue sky"></div>
  <h1 class="brand-name">FRÜST</h1>
  <div class="strapline-band">
    <div class="packshots packshots--cartons">
      <div class="packshot packshot--carton" role="img" aria-label="Frozen Cosmopolitan carton pack"></div>
      <div class="packshot packshot--carton" role="img" aria-label="Frozen Mojito carton pack"></div>
      <div class="packshot packshot--carton" role="img" aria-label="Frozen Lychee Martini carton pack"></div>
    </div>
    <p class="strapline">
      <span class="strapline__line">Authentic bar-quality cocktails made with the finest natural ingredients.</span>
      <span class="strapline__line">No mixing, no mess, no hassle. Just freeze, squeeze &amp; enjoy!</span>
    </p>
    <div class="packshots packshots--pouches">
      <div class="packshot packshot--pouch" role="img" aria-label="Frozen Cosmopolitan pouch"></div>
      <div class="packshot packshot--pouch" role="img" aria-label="Frozen Mojito pouch"></div>
      <div class="packshot packshot--pouch" role="img" aria-label="Frozen Lychee Martini pouch"></div>
    </div>
  </div>
</section>

<section class="flyer flyer--back">
  <article class="flavour flavour--cosmopolitan">
    <h2 class="flavour__kind">FROZEN</h2>
    <h3 class="flavour__name">Cosmopolitan</h3>
    <p class="flavour__tagline">The sophisticated Cosmopolitan</p>
    <p class="flavour__copy">A delicious combination of cranberries,<br>lime, orange liqueur and pure,<br>triple distilled vodka.</p>
    <p class="flavour__copy">Made just like the New York classic,<br>this perfectly pink cocktail<br>is best served FRÜST.</p>
  </article>
  <article class="flavour flavour--mojito">
    <h2 class="flavour__kind">FROZEN</h2>
    <h3 class="flavour__name">Mojito</h3>
    <p class="flavour__tagline">The classic Mojito</p>
    <p class="flavour__copy">A refreshing blend of mint,<br>lime and sugar muddled with smooth,<br>barrel-aged white rum.</p>
    <p class="flavour__copy">Made to the orginal Cuban recipe,<br>this zesty cocktail<br>is best served FRÜST.</p>
  </article>
  <article class="flavour flavour--lychee">
    <h2 class="flavour__kind">FROZEN</h2>
    <h3 class="flavour__name">Lychee Martini</h3>
    <p class="flavour__tagline">The exotic Lychee Martini</p>
    <p class="flavour__copy">Aromatic lychees blended with pure,<br>triple distilled vodka.</p>
    <p class="flavour__copy">Designed as a modern twist<br>to the classic Martini,<br>this fragrant cocktail<br>is best served FRÜST.</p>
  </article>

  <div class="corner-mark">FRÜST</div>

  <footer class="contact">
    <span class="contact__item"><span class="contact__dot"></span>frustcocktails</span>
    <span class="contact__divider">|</span>
    <span class="contact__item">www.frustcocktails.example</span>
    <span class="contact__divider">|</span>
    <span class="contact__item"><span class="contact__dot contact__dot--twitter"></span>frustcocktails</span>
  </footer>
</section>

</body>
</html>
```